Cedar Lane Bail Bonds Signboard Ad

I need a signboard ad that will be posted at a jail. We are a bail bond company and we bail people out of jail. The inmate/customer will call our company when they see our signboard ad posted inside a jail. The goal of the signboard ad is to get the attention of a person in custody and to stand out from the competition. The signboard ad is about 5x7. Open to any colors that will make it stand out. The content of the signboard ad must have "Cedar Lane Bail Bonds" and our company phone number: (555) 318-2047. We want to emphasize we can get them out of jail quick and fast, was thinking maybe a catch phrase of "Blast outta Jail" or "Cedar Lane to Freedom". We don't have a logo. I will upload an attachment to show what the competition looks like. As you will see in the upload, my ad will go along with my competition. Also, I'm open to any creative ideas that will make my signboard ad stand out. Thank You.

Target Market(s)

People in jail.

Requirements
Must have
• Cedar Lane Bail Bonds

(555) 318-2047
Nice to have
• I'm open to catch phrases that will get attention, for example "Blast outta Jail" or "Cedar Lane to Freedom". I do not have a company logo, if you can create a company logo, would be nice, was thinking an image of a rocket blasting off, The name of company is Cedar Lane Bail Bonds.

```html
<!DOCTYPE html>
<html lang="en">
<head>
<meta charset="utf-8">
<title>Cedar Lane Bail Bonds Signboard</title>
<link href="https://fonts.googleapis.com/css2?family=Anton&family=Bowlby+One&display=swap" rel="stylesheet">
<style>
  :root {
    --backdrop: #000000;
    --sign-white: #ffffff;
    --brand-blue: #0a72be;
    --wave-light: #a9bfe4;
    --wave-mid: #5f8fd0;
    --ink: #000000;
    --shadow-grey: #6d6e71;
  }
  html, body {
    margin: 0;
    padding: 0;
    width: 1200px;
    height: 934px;
    overflow: hidden;
    background: var(--backdrop);
  }
  .signboard {
    display: block;
    width: 1200px;
    height: 934px;
  }
  .headline {
    font-family: "Bowlby One", "Arial Black", sans-serif;
    font-size: 176px;
  }
  .headline-halo {
    fill: var(--sign-white);
    stroke: var(--sign-white);
    stroke-width: 22;
    stroke-linejoin: round;
  }
  .headline-shadow {
    fill: var(--shadow-grey);
    stroke: var(--shadow-grey);
    stroke-width: 8;
    stroke-linejoin: round;
  }
  .headline-face {
    fill: url(#chromeBlue);
    stroke: var(--ink);
    stroke-width: 4;
    stroke-linejoin: round;
    paint-order: stroke;
  }
  .phone {
    font-family: "Anton", "Impact", sans-serif;
    font-size: 186px;
    fill: var(--sign-white);
    stroke: var(--ink);
    stroke-width: 7;
    stroke-linejoin: round;
    paint-order: stroke;
  }
</style>
</head>
<body>
<svg class="signboard" viewBox="0 0 1200 934" xmlns="http://www.w3.org/2000/svg">
  <defs>
    <linearGradient id="chromeBlue" x1="0" y1="0" x2="0" y2="1">
      <stop offset="0" stop-color="#0a72be"/>
      <stop offset="0.42" stop-color="#0a72be"/>
      <stop offset="0.5" stop-color="#e6ecf7"/>
      <stop offset="0.55" stop-color="#ffffff"/>
      <stop offset="0.62" stop-color="#0a72be"/>
      <stop offset="1" stop-color="#0a72be"/>
    </linearGradient>
    <linearGradient id="waveFill" x1="0" y1="0" x2="1" y2="1">
      <stop offset="0" stop-color="#2f7fca"/>
      <stop offset="0.5" stop-color="#5b8fd0"/>
      <stop offset="1" stop-color="#1d78c2"/>
    </linearGradient>
    <linearGradient id="waveBottom" x1="0" y1="0" x2="0" y2="1">
      <stop offset="0" stop-color="#ffffff" stop-opacity="0"/>
      <stop offset="1" stop-color="#0a72be" stop-opacity="0.8"/>
    </linearGradient>
    <linearGradient id="cornerGlow" x1="1" y1="0" x2="0.6" y2="0.5">
      <stop offset="0" stop-color="#e2eaf7"/>
      <stop offset="1" stop-color="#ffffff" stop-opacity="0"/>
    </linearGradient>
    <clipPath id="signClip">
      <rect x="134" y="134" width="932" height="666"/>
    </clipPath>
  </defs>

  <g class="sign-panel" clip-path="url(#signClip)">
    <rect x="134" y="134" width="932" height="666" fill="var(--sign-white)"/>
    <rect x="800" y="134" width="266" height="160" fill="url(#cornerGlow)"/>
    <path class="wave-band" d="M134 484 C300 560 520 580 700 560 C860 540 980 540 1066 590 L1066 800 L134 800 Z" fill="url(#waveFill)"/>
    <path class="wave-depth" d="M134 560 L1066 560 L1066 800 L134 800 Z" fill="url(#waveBottom)"/>
    <path class="wave-highlight" d="M134 505 C300 575 500 590 700 572 C860 556 980 560 1066 600 L1066 612 C980 572 860 570 700 584 C500 600 300 590 134 522 Z" fill="var(--wave-light)" opacity="0.7"/>
    <path class="wave-line" d="M300 578 C500 572 700 545 860 548 C960 550 1020 570 1066 596" fill="none" stroke="var(--sign-white)" stroke-width="3"/>
  </g>

  <g class="headline" transform="skewX(-8)">
    <g transform="translate(36 0)">
      <text class="headline-halo" x="176" y="352" textLength="850" lengthAdjust="spacingAndGlyphs">CEDAR LANE</text>
      <text class="headline-shadow" x="184" y="360" textLength="850" lengthAdjust="spacingAndGlyphs">CEDAR LANE</text>
      <text class="headline-face" x="176" y="352" textLength="850" lengthAdjust="spacingAndGlyphs">CEDAR LANE</text>

      <text class="headline-halo" x="176" y="526" textLength="850" lengthAdjust="spacingAndGlyphs">BAIL BONDS</text>
      <text class="headline-shadow" x="184" y="534" textLength="850" lengthAdjust="spacingAndGlyphs">BAIL BONDS</text>
      <text class="headline-face" x="176" y="526" textLength="850" lengthAdjust="spacingAndGlyphs">BAIL BONDS</text>
    </g>
  </g>

  <text class="phone" x="172" y="746" textLength="856" lengthAdjust="spacingAndGlyphs">(555) 318-2047</text>
</svg>
</body>
</html>
```